The name of the company is Dorvane Holdings, LLC. I would like a business card with a logo.

On the top left, I would like a logo design of a crown and I would like Dorvane over the top of the crown while Investments on the bottom. Please see attached files as an example of crown and positioning of Dorvane Holdings. Then I would like the letters DH in the middle(see picture).

Colors

Designer to choose colors to be used in the design.

```html
<!DOCTYPE html>
<html lang="en">
<head>
<meta charset="utf-8">
<title>Dorvane Holdings, LLC — Business Card</title>
<link rel="stylesheet" href="https://fonts.googleapis.com/css2?family=Lato:wght@400;700&display=swap">
<style>
  :root {
    --page-bg: #8b6b47;
    --card-bg: #000000;
    --gold: #e9d0a0;
    --soft-grey: #c9c9c9;
    --crown-red: #8e1a1f;
    --crown-gold: #b98a3e;
    --plume-green: #2f5a45;
  }
  * { margin: 0; padding: 0; box-sizing: border-box; }
  html, body { width: 1200px; height: 1023px; overflow: hidden; }
  body {
    background: var(--page-bg);
    font-family: "Lato", sans-serif;
    position: relative;
  }
  .card {
    position: absolute;
    left: 248px;
    width: 681px;
    height: 396px;
    background: var(--card-bg);
    box-shadow: -6px 6px 0 rgba(0,0,0,0.55);
  }
  .card--front { top: 87px; }
  .card--back { top: 542px; }

  .holder-name {
    position: absolute; left: 30px; top: 41px;
    font-size: 31px; font-weight: 700; color: var(--gold);
    letter-spacing: 0.2px;
  }
  .holder-role {
    position: absolute; left: 30px; top: 81px;
    font-size: 17px; color: var(--soft-grey);
  }
  .address {
    position: absolute; left: 30px; top: 232px;
    font-size: 15px; line-height: 20px; color: var(--soft-grey);
  }
  .contact-list {
    position: absolute; left: 30px; top: 290px;
    list-style: none; font-size: 15px; color: var(--soft-grey);
  }
  .contact-list li {
    display: flex; align-items: center; gap: 10px; height: 20px; margin-bottom: 7px;
  }
  .contact-list svg { width: 15px; height: 15px; fill: var(--soft-grey); }

  .crown-mark {
    position: absolute;
    border-radius: 40% 40% 12% 12%;
    background: linear-gradient(180deg, var(--plume-green) 0%, var(--plume-green) 30%, var(--crown-red) 55%, var(--crown-gold) 100%);
  }
  .card--front .crown-mark { left: 441px; top: 87px; width: 130px; height: 186px; }
  .card--back .crown-mark { left: 253px; top: 39px; width: 178px; height: 256px; }

  .company-name {
    position: absolute; left: 0; width: 100%;
    color: var(--gold); font-weight: 400; text-align: center; white-space: nowrap;
  }
  .card--front .company-name { left: 367px; width: 274px; top: 284px; font-size: 26px; }
  .card--back .company-name { top: 311px; font-size: 37px; }
</style>
</head>
<body>
  <section class="card card--front">
    <h1 class="holder-name">Karin Voslev, MBA</h1>
    <p class="holder-role">Founder / CEO</p>
    <p class="address">418 Larkmoor Road, Suite 200<br>Ashcombe Ridge, CA. 90911</p>
    <ul class="contact-list">
      <li>
        <svg viewBox="0 0 24 24" aria-hidden="true"><path d="M6.6 10.8a15.1 15.1 0 0 0 6.6 6.6l2.2-2.2a1 1 0 0 1 1-.25 11.4 11.4 0 0 0 3.6.57 1 1 0 0 1 1 1V20a1 1 0 0 1-1 1A17 17 0 0 1 3 4a1 1 0 0 1 1-1h3.5a1 1 0 0 1 1 1c0 1.25.2 2.45.57 3.57a1 1 0 0 1-.25 1z"/></svg>
        (310) 555-0143
      </li>
      <li>
        <svg viewBox="0 0 24 24" aria-hidden="true"><path d="M2 5h20v14H2z M3.5 6.5 12 13l8.5-6.5v1.8L12 15 3.5 8.3z" fill-rule="evenodd"/></svg>
        k.voslev@dorvaneholdings.com
      </li>
    </ul>
    <div class="crown-mark" role="img" aria-label="Jewelled crown emblem with plume"></div>
    <p class="company-name">Dorvane Holdings, LLC</p>
  </section>

  <section class="card card--back">
    <div class="crown-mark" role="img" aria-label="Jewelled crown emblem with plume"></div>
    <p class="company-name">Dorvane Holdings, LLC</p>
  </section>
</body>
</html>
```